New Business Card Design Project

Want a simple but attention grabbing business card. Back Side having mainly our logo and basic info-the front side a typical business card.

Contact Information for Business Card

Hearth & Basin Works
218 NW Larkfield Rd. Suite 207
Brenton Falls, Kansas 66012

phone- 515.284.7093

website is -hbwplains.com

```html
<!DOCTYPE html>
<html lang="en">
<head>
<meta charset="utf-8">
<title>Hearth &amp; Basin Works – Business Card</title>
<link href="https://fonts.googleapis.com/css2?family=Lato:wght@400;700;900&display=swap" rel="stylesheet">
<style>
  :root {
    --backdrop: #d2d3cf;
    --card-white: #ffffff;
    --card-navy: #0c1628;
    --accent-orange: #f15a24;
    --text-grey: #6b6b6b;
  }
  * { box-sizing: border-box; margin: 0; padding: 0; }
  html, body {
    width: 1200px; height: 801px; overflow: hidden;
    background: var(--backdrop);
    font-family: "Lato", sans-serif;
  }
  .canvas {
    width: 1200px; height: 801px;
    display: flex; flex-direction: column;
    align-items: center; justify-content: center; gap: 36px;
  }
  .card {
    width: 640px; height: 360px;
    position: relative;
    box-shadow: 0 10px 24px rgba(0,0,0,0.18);
  }
  .card--front { background: var(--card-white); display: flex; align-items: center; }
  .card--back { background: var(--card-navy); display: flex; align-items: center; justify-content: center; }

  .brand-name {
    display: flex; align-items: center; gap: 12px;
    color: var(--accent-orange);
    font-weight: 900;
    line-height: 1.05;
  }
  .brand-name__mark {
    width: 14px; height: 14px; background: var(--accent-orange); flex: none;
  }
  .card--front .brand-block {
    width: 290px; padding-left: 48px;
  }
  .card--front .brand-name { font-size: 30px; }
  .card--back .brand-name { font-size: 44px; }

  .divider {
    width: 2px; height: 150px; background: var(--accent-orange);
    margin: 0 34px 0 6px;
  }
  .details { color: var(--text-grey); }
  .details__name {
    color: var(--accent-orange); font-weight: 900;
    font-size: 24px; letter-spacing: 0.5px; text-transform: uppercase;
  }
  .details__role { font-size: 16px; margin: 2px 0 18px; }
  .details__address { font-size: 15px; line-height: 1.35; margin-bottom: 4px; }
  .contact-list { list-style: none; font-size: 15px; line-height: 1.45; }
  .contact-list li { display: flex; align-items: center; gap: 8px; }
  .contact-list svg { width: 14px; height: 14px; flex: none; }
</style>
</head>
<body>
<main class="canvas">
  <section class="card card--front" aria-label="Business card front">
    <div class="brand-block">
      <div class="brand-name"><span class="brand-name__mark"></span><span>Hearth &amp; Basin Works</span></div>
    </div>
    <div class="divider"></div>
    <div class="details">
      <p class="details__name">Dale Ferrin</p>
      <p class="details__role">Director</p>
      <p class="details__address">218 NW Larkfield Rd. Suite 207<br>Brenton Falls, Kansas 66012</p>
      <ul class="contact-list">
        <li>
          <svg viewBox="0 0 14 14" aria-hidden="true"><path d="M3 1.5l2.2 2.4-1.2 1.4a7 7 0 0 0 4.7 4.7l1.4-1.2 2.4 2.2-1.3 1.6C6.5 12.2 1.8 7.5 1.4 2.8z" fill="var(--accent-orange)"/></svg>
          515.284.7093
        </li>
        <li>
          <svg viewBox="0 0 14 14" aria-hidden="true"><rect x="1" y="3" width="12" height="8.5" fill="var(--accent-orange)"/><path d="M1 3l6 5 6-5" fill="none" stroke="#fff" stroke-width="1.2"/></svg>
          info@hbwplains.com
        </li>
        <li>
          <svg viewBox="0 0 14 14" aria-hidden="true"><circle cx="7" cy="7" r="6" fill="var(--accent-orange)"/><path d="M1 7h12M7 1v12M3 3.5h8M3 10.5h8" stroke="#fff" stroke-width="0.9" fill="none"/></svg>
          www.hbwplains.com
        </li>
      </ul>
    </div>
  </section>

  <section class="card card--back" aria-label="Business card back">
    <div class="brand-name"><span class="brand-name__mark"></span><span>Hearth &amp; Basin Works</span></div>
  </section>
</main>
</body>
</html>
```